Anzeigengestaltung für Stellenanzeige
Zielgruppe
Wir sind ein Abrechnungsunternehmen das für Zahnärzte die zahnmedizinische und zahntechnische Abrechnung von extern übernimmt.
Aufgrund einer Erweiterung suchen wir neues Personal welches uns unterstützt. Deshalb benötigen wir einen Stellenanzeige.
Wir suchen Personal - zahnmedizinische Fachangestellte mit Erfahrung in der Abrechnung
Abkürzungen: ZFA oder ZMV beides gewünscht wenn Abrechnungskenntnisse vorhanden sind.
Aufgabenstellung
Bitte Stellenanzeige unserer Website anpassen, www.zahnkanzleimerwen.de
logo bitte con Website übernehmen.
Moderne Gestaltung
Wir bieten:
-Anstellung Teilzeit oder Vollzeit
-Ein motiviertes und kompetentes Team
-Fort- und Weitermöglichkeiten
-Flexible Arbeits- und Urlaubszeiten
-Attraktive leistungsgerechte Bezahlung
Ihr Profil
Um die Stelle gut ausfüllen zu können, wünschen wir uns von Ihnen:
Abgeschlossene Ausbildung zum/zur Zahnmedizinische Fachangestellte, Zahnmedizinische Verwaltungsfachangestellte (m/w/d)
Selbstständiges Arbeiten und Einsatzbereitschaft
Gute PC-Kenntnisse und sicherer Umgang mit gängigen Office-Anwendungen
Erfahrung in der zahmedizinischen Abrechnung
Sorgfalt, Teamfähigkeit
Engagement und Freude am Beruf
Wir haben Ihr Interesse geweckt dann senden Sie uns Ihre Bewerbung an: t.brellmann@zahnkanzleimerwen.de
------Beispiel----------
Gerne auch eigene Beispiele....

```html
<!DOCTYPE html>
<html lang="de">
<head>
<meta charset="utf-8">
<title>Stellenanzeige – Kanzlei Merwen</title>
<link rel="stylesheet" href="https://fonts.googleapis.com/css2?family=Poppins:wght@300;400;500&display=swap">
<style>
  :root {
    --bg-dark: #161616;
    --bg-mid: #262626;
    --band: #b3b0a9;
    --ink-dark: #111111;
    --ink-light: #f2f2f2;
    --heading-beige: #ddd3c6;
    --logo-beige: #d9cdbd;
    --muted: #b8b3ac;
  }
  * { margin: 0; padding: 0; box-sizing: border-box; }
  html, body { width: 844px; height: 1200px; overflow: hidden; background: var(--bg-dark); }
  .ad {
    position: relative;
    width: 844px;
    height: 1200px;
    overflow: hidden;
    font-family: "Poppins", sans-serif;
    color: var(--ink-light);
    background:
      radial-gradient(ellipse at 30% 40%, #2a2a2a 0%, transparent 60%),
      radial-gradient(ellipse at 80% 75%, #252525 0%, transparent 55%),
      linear-gradient(160deg, var(--bg-mid) 0%, var(--bg-dark) 70%, #0f0f0f 100%);
    text-align: center;
  }
  .brand { position: absolute; top: 44px; left: 0; width: 100%; }
  .brand-name {
    display: inline-flex; align-items: center; gap: 10px;
    font-size: 33px; font-weight: 500; color: var(--logo-beige); letter-spacing: -0.5px;
  }
  .brand-dot { width: 12px; height: 12px; border-radius: 50%; background: var(--logo-beige); }
  .brand-tagline { margin-top: 10px; font-size: 13px; font-weight: 400; color: var(--logo-beige); }

  .headline-band {
    position: absolute; top: 145px; left: 0; width: 100%; height: 168px;
    background: var(--band); color: var(--ink-dark); padding-top: 26px;
  }
  .headline { font-size: 40px; font-weight: 400; line-height: 1.2; }
  .headline-sub { margin-top: 16px; font-size: 16.5px; font-weight: 300; line-height: 22px; }

  .section-title { font-size: 28px; font-weight: 300; color: var(--heading-beige); }
  .offer { position: absolute; top: 362px; left: 0; width: 100%; }
  .offer-list { list-style: none; margin-top: 16px; font-size: 16px; font-weight: 300; line-height: 21px; }

  .profile { position: absolute; top: 563px; left: 0; width: 100%; font-size: 15.5px; font-weight: 300; line-height: 21px; }
  .profile-intro { margin-top: 10px; }
  .profile-block { margin-top: 19px; }

  .apply {
    position: absolute; top: 960px; left: 55px; text-align: left;
    font-size: 22.5px; font-weight: 300; line-height: 29px;
  }
  .apply-mail { color: var(--muted); }

  .team-photo {
    position: absolute; left: 548px; top: 855px; width: 250px; height: 345px;
    background: linear-gradient(180deg, #3a342c 0%, #8a7a64 45%, #1b1b1b 100%);
    border-radius: 40px 40px 0 0;
  }
</style>
</head>
<body>
<main class="ad">
  <header class="brand">
    <div class="brand-name"><span class="brand-dot"></span>Kanzlei Merwen</div>
    <div class="brand-tagline">Zahnärztliche Abrechnung &amp; Managment</div>
  </header>

  <section class="headline-band">
    <h1 class="headline">Wir suchen Personal</h1>
    <p class="headline-sub">- zahnmedizinische Fachangestellte mit Erfahrung in der Abrechnung<br>ZFA oder ZMV beides gewünscht wenn Abrechnungskenntnisse vorhanden sind</p>
  </section>

  <section class="offer">
    <h2 class="section-title">Wir bieten:</h2>
    <ul class="offer-list">
      <li>-Anstellung Teilzeit oder Vollzeit</li>
      <li>-Ein motiviertes und kompetentes Team</li>
      <li>-Fort- und Weitermöglichkeiten</li>
      <li>-Flexible Arbeits- und Urlaubszeiten</li>
      <li>-Attraktive leistungsgerechte Bezahlung</li>
    </ul>
  </section>

  <section class="profile">
    <h2 class="section-title">Ihr Profil:</h2>
    <p class="profile-intro">Um die Stelle gut ausfüllen zu können, wünschen wir uns von Ihnen:</p>
    <p class="profile-block">Abgeschlossene Ausbildung zum/zur Zahnmedizinische Fachangestellte,<br>Zahnmedizinische Verwaltungsfachangestellte (m/w/d)</p>
    <p class="profile-block">Selbstständiges Arbeiten und Einsatzbereitschaft<br>Gute PC-Kenntnisse und sicherer Umgang mit gängigen Office-Anwendungen<br>Erfahrung in der zahnmedizinischen Abrechnung<br>Sorgfalt, Teamfähigkeit<br>Engagement und Freude am Beruf</p>
  </section>

  <footer class="apply">
    <p>Wir haben Ihr Interesse geweckt dann<br>senden Sie uns Ihre Bewerbung an:</p>
    <p class="apply-mail">t.brellmann@zahnkanzleimerwen.de</p>
  </footer>

  <div class="team-photo" role="img" aria-label="Foto von zwei Mitarbeiterinnen in beigen Blazern"></div>
</main>
</body>
</html>
```